Brava Nest (Smart Home, Installation, Repair Industry) (Contest)

Looking for a website design for my company
Services we offer:
Phone Repair
TV Mounting
Security Camera Installation
Networking / Wi-Fi
Smart Home Services
IT Support

Looking for a website similar to trovely.example

Few tabs
About Us
Contact Us
Areas Served
Pricing and Services

```html
<!DOCTYPE html>
<html lang="en">
<head>
<meta charset="utf-8">
<title>Brava Nest — Home Tech Installation &amp; Repair</title>
<link href="https://fonts.googleapis.com/css2?family=Poppins:wght@300;400;500;600;700&family=Roboto:wght@300;500;700&display=swap" rel="stylesheet">
<style>
:root{
  --ink:#3b3470;
  --ink-soft:#6e6a8f;
  --orange:#f7941d;
  --violet:#9166d4;
  --mint:#5fd68e;
  --navy:#21284f;
  --footer:#2b3160;
  --mist:#f4f4f9;
  --line:#e3e3ee;
  --white:#ffffff;
}
*{box-sizing:border-box;margin:0;padding:0}
html,body{width:1200px;height:2799px;overflow:hidden}
body{position:relative;background:var(--white);font-family:'Poppins',sans-serif;color:var(--ink)}
.abs{position:absolute}

/* hero */
.hero{position:absolute;left:0;top:0;width:1200px;height:600px;overflow:hidden}
.hero-photo{position:absolute;inset:0;background:radial-gradient(ellipse at 70% 40%,#6d6aa8 0%,#45437f 45%,#2e2c62 100%)}
.hero-wave{position:absolute;left:0;top:0}
.brand{font-family:'Poppins',sans-serif;font-weight:700;color:var(--orange);font-size:26px;letter-spacing:-.3px;white-space:nowrap}
.nav{position:absolute;top:38px;left:0;width:1200px;height:24px}
.nav a{position:absolute;top:0;color:var(--white);text-decoration:none;font-size:14px;font-weight:500;white-space:nowrap}
.social-dot{position:absolute;top:46px;width:7px;height:7px;border-radius:50%;background:var(--white)}
.hero-title{position:absolute;top:192px;left:0;width:1200px;text-align:center;color:var(--white);font-family:'Roboto',sans-serif;font-weight:300;font-size:40px;line-height:53px;letter-spacing:-.5px}
.hero-title strong{font-weight:700}
.hero-sub{position:absolute;top:313px;left:0;width:1200px;text-align:center;color:#e6e4f4;font-size:14px;font-weight:300}
.btn{position:absolute;left:534px;top:371px;width:131px;height:35px;background:var(--orange);color:var(--white);font-size:12px;font-weight:600;text-align:center;line-height:35px;border-radius:2px}

/* headings */
.section-title{position:absolute;left:0;width:1200px;text-align:center;font-size:19px;font-weight:500;line-height:26px;color:var(--ink)}

/* service cards */
.service{position:absolute;top:742px;width:171px;height:194px;border:1px solid var(--line);background:var(--white);text-align:center}
.service.active{border-top:4px solid var(--orange);box-shadow:0 6px 18px rgba(60,55,120,.08);border-left-color:#fff;border-right-color:#fff}
.service svg{position:absolute;left:62px;top:30px}
.service h3{position:absolute;top:98px;left:0;width:100%;font-size:12px;font-weight:600;line-height:17px;color:var(--ink)}
.service p{position:absolute;left:0;width:100%;font-size:10.5px;line-height:17px;color:var(--ink-soft);white-space:nowrap}
.dot{position:absolute;top:961px;width:6px;height:6px;border-radius:50%;background:#b8b6d3}
.dot.on{background:var(--orange)}

/* features */
.feature-title{position:absolute;font-family:'Roboto',sans-serif;font-size:29px;line-height:36px;color:var(--ink);white-space:nowrap}
.feature-title strong{font-weight:700;display:block}
.feature-title span{font-weight:300;display:block}
.feature-text{position:absolute;font-size:11px;line-height:23px;color:var(--ink-soft);font-weight:300;white-space:nowrap}
.block{position:absolute}
.soft-shadow{position:absolute;height:14px;border-radius:50%;background:radial-gradient(ellipse at center,rgba(40,40,80,.18),rgba(40,40,80,0) 70%)}

/* faq */
.faq-band{position:absolute;left:0;top:1697px;width:1200px;height:401px;background:var(--mist)}
.faq{position:absolute;top:1853px;width:234px;height:169px;background:var(--white);border:1px solid var(--line)}
.faq.active{border-top:4px solid #d6d6e2;box-shadow:0 6px 18px rgba(60,55,120,.10)}
.faq h4{position:absolute;left:32px;top:29px;font-size:12px;font-weight:600;color:var(--ink);white-space:nowrap}
.faq .badge{position:absolute;right:24px;top:29px;width:16px;height:16px;border-radius:50%;color:#fff;font-size:9px;font-weight:600;text-align:center;line-height:16px}
.faq p{position:absolute;left:32px;top:64px;font-size:10.5px;line-height:19px;color:var(--ink-soft);white-space:nowrap}

/* testimonials */
.round{position:absolute;border-radius:50%}
.arrow-btn{position:absolute;top:2267px;width:26px;height:26px;border-radius:50%;border:1px solid #eeeef4;background:#fff}
.arrow-btn svg{position:absolute;left:8px;top:8px}
.quote-text{position:absolute;left:300px;width:600px;top:2350px;text-align:center;font-size:11px;line-height:23px;color:var(--ink-soft);font-weight:300}
.quote-name{position:absolute;left:0;width:1200px;top:2403px;text-align:center;font-size:11px;color:var(--ink-soft);font-weight:400}
.tdot{position:absolute;top:2446px;width:4px;height:4px;border-radius:50%;background:#d0cfe0}

/* footer */
.footer-wave{position:absolute;left:0;top:2480px}
.foot-social{position:absolute;top:2646px;width:26px;height:26px;border-radius:50%;background:#5d6188}
.foot-rule{position:absolute;left:229px;top:2711px;width:742px;height:1px;background:#6b6f95}
.copyright{position:absolute;top:2745px;left:0;width:1200px;text-align:center;font-size:10.5px;color:#a9abc6}
.copyright b{color:var(--orange);font-weight:500}
</style>
</head>
<body>

<header class="hero">
  <div class="hero-photo" role="img" aria-label="Technician's gloved hands repairing a phone with a precision screwdriver, tinted in deep purple"></div>
  <svg class="hero-wave" width="1200" height="600" viewBox="0 0 1200 600" aria-hidden="true">
    <path d="M0 410 C120 330 200 320 300 260 C380 210 420 90 520 0 L0 0 Z" fill="rgba(255,255,255,.05)"/>
    <path d="M0 598 C300 570 700 565 1200 578 L1200 600 L0 600 Z" fill="#fff"/>
  </svg>
  <div class="brand abs" style="left:230px;top:30px">Brava Nest</div>
  <nav class="nav">
    <a style="left:489px">About Us</a>
    <a style="left:577px">Pricing &amp; Services</a>
    <a style="left:723px">Areas Served</a>
    <a style="left:839px">Contact</a>
  </nav>
  <span class="social-dot" style="left:931px"></span>
  <span class="social-dot" style="left:946px"></span>
  <span class="social-dot" style="left:962px"></span>
  <h1 class="hero-title">We Bring <strong>Your Devices</strong><br>Back To Life</h1>
  <p class="hero-sub">The best technicians in your neighborhood.</p>
  <div class="btn">Book a Service</div>
</header>

<h2 class="section-title" style="top:658px">Brava Nest is pretty big thing to explore<br>Checkout Services</h2>

<article class="service" style="left:229px">
  <svg width="48" height="44" viewBox="0 0 48 44" fill="none" stroke="#3b3470" stroke-width="1.6">
    <rect x="12" y="4" width="22" height="38" rx="3"/><rect x="6" y="8" width="16" height="34" rx="2"/>
    <path d="M38 10a6 6 0 0 1 6 0M40 13a3 3 0 0 1 2 0"/><circle cx="10" cy="13" r="1"/>
  </svg>
  <h3>Phone Repair</h3>
  <p style="top:132px">Fix your phone at your<br>home, office</p>
</article>
<article class="service active" style="left:419px">
  <svg width="48" height="44" viewBox="0 0 48 44" fill="none" stroke="#f7941d" stroke-width="1.8">
    <rect x="4" y="4" width="40" height="28" rx="2"/><rect x="8" y="8" width="32" height="20"/>
    <path d="M18 32v5h12v-5M12 40h24"/>
  </svg>
  <h3 style="top:94px">TV Mounting</h3>
  <p style="top:128px">Let us do the heavy<br>lifting &nbsp;for yourm new TV</p>
</article>
<article class="service" style="left:610px">
  <svg width="48" height="44" viewBox="0 0 48 44" fill="none" stroke="#3b3470" stroke-width="1.6">
    <path d="M12 6l32 10-4 10-30-8z"/><path d="M18 20l-2 8h-6M8 22v14M8 30h8"/><circle cx="36" cy="17" r="2"/>
  </svg>
  <h3>Security Camera<br>Installation</h3>
  <p style="top:148px">Lorem Ipsum is simply</p>
</article>
<article class="service" style="left:800px">
  <svg width="48" height="44" viewBox="0 0 48 44" fill="none" stroke="#3b3470" stroke-width="1.6">
    <path d="M4 14a28 28 0 0 1 40 0M10 20a20 20 0 0 1 28 0M16 26a12 12 0 0 1 16 0"/>
    <circle cx="24" cy="34" r="3"/><circle cx="38" cy="30" r="3"/><path d="M34 42a4 4 0 0 1 8 0"/>
  </svg>
  <h3>Networking / Wi-Fi</h3>
  <p style="top:132px">Lorem Ipsum is simply<br>dummy text of the</p>
</article>
<span class="dot" style="left:621px"></span>
<span class="dot on" style="left:635px"></span>
<span class="dot" style="left:649px"></span>

<h2 class="feature-title" style="left:643px;top:1044px"><strong>Trusted technicians</strong><span>in your neighborhood</span></h2>
<p class="feature-text" style="left:643px;top:1126px">Lorem Ipsum is simply dummy text of the printing and<br>typesetting industry. Lorem Ipsum has been the industry's<br>standard dummy text ever since the 1500s,</p>

<div class="soft-shadow" style="left:239px;top:1341px;width:261px"></div>
<div class="soft-shadow" style="left:652px;top:1517px;width:293px"></div>
<div class="block" style="left:441px;top:1138px;width:159px;height:174px;background:var(--orange)"></div>
<div class="block" style="left:619px;top:1229px;width:63px;height:67px;background:var(--violet)"></div>
<div class="block" style="left:518px;top:1331px;width:63px;height:67px;background:var(--mint)"></div>
<div class="block" style="left:601px;top:1315px;width:158px;height:174px;background:var(--navy)"></div>

<h2 class="feature-title" style="right:640px;top:1422px;text-align:right"><strong>Guaranteed Parts</strong><span>&amp; service + 24/7 support</span></h2>
<p class="feature-text" style="right:639px;top:1508px;text-align:right">It is important to stay focused on saving money in any way you<br>can. We help you monitor your spending habits so you can<br>easily spot and cut any unnecessary expenses. Simply join<br>today to get started!</p>

<section class="faq-band"></section>
<h2 class="section-title" style="top:1768px">Do you have any questions?<br>Findout answers:</h2>
<article class="faq" style="left:229px">
  <h4>Lorem Ipsum is simply</h4><span class="badge" style="background:#a39be0">?</span>
  <p>Lorem Ipsum is simply dummy<br>text of the printing and<br>typesetting industry. Lorem Ipsum<br>has been the industry's text ever</p>
</article>
<article class="faq active" style="left:483px">
  <h4 style="top:26px">Lorem Ipsum is simply</h4><span class="badge" style="background:#f9bf4a;top:26px">?</span>
  <p style="top:61px">Lorem Ipsum is simply dummy<br>text of the printing and<br>typesetting industry. Lorem Ipsum<br>has been the industry's text ever</p>
</article>
<article class="faq" style="left:736px">
  <h4>Lorem Ipsum is simply</h4><span class="badge" style="background:#f38fb3">?</span>
  <p>Lorem Ipsum is simply dummy<br>text of the printing and<br>typesetting industry. Lorem Ipsum<br>has been the industry's text ever</p>
</article>

<h2 class="section-title" style="top:2155px">What users think about<br>Users testimonails:</h2>
<div class="arrow-btn" style="left:386px"><svg width="10" height="10" viewBox="0 0 10 10" fill="none" stroke="#8a88a8" stroke-width="1.2"><path d="M6 2L3 5l3 3"/></svg></div>
<div class="arrow-btn" style="left:805px"><svg width="10" height="10" viewBox="0 0 10 10" fill="none" stroke="#8a88a8" stroke-width="1.2"><path d="M4 2l3 3-3 3"/></svg></div>
<div class="round" role="img" aria-label="Customer portrait" style="left:522px;top:2255px;width:50px;height:50px;background:#efefef"></div>
<div class="round" role="img" aria-label="Customer portrait" style="left:644px;top:2255px;width:50px;height:50px;background:#efefef"></div>
<div class="round" role="img" aria-label="Featured customer portrait" style="left:567px;top:2239px;width:82px;height:82px;background:#cfcfcf"></div>
<div class="round" style="left:592px;top:2300px;width:32px;height:32px;background:var(--orange);border:2px solid #fff;color:#fff;font-size:14px;font-weight:700;text-align:center;line-height:30px">&ldquo;</div>
<p class="quote-text">Lorem Ipsum is simply dummy text of the printing and typesetting industry. Lorem Ipsum<br>has been the industry's standard dummy text ever since the 1500s,</p>
<p class="quote-name">Lorem Ipsum</p>
<span class="tdot" style="left:582px;width:6px;height:6px;top:2445px;background:none;border:1px solid var(--orange)"></span>
<span class="tdot" style="left:593px"></span>
<span class="tdot" style="left:602px"></span>
<span class="tdot" style="left:611px"></span>
<span class="tdot" style="left:620px"></span>

<footer>
  <svg class="footer-wave" width="1200" height="319" viewBox="0 0 1200 319" aria-hidden="true">
    <path d="M0 94 C60 30 120 7 179 7 C280 7 330 132 434 132 C560 132 640 7 760 7 C900 7 940 121 1032 121 C1110 121 1160 60 1200 18 L1200 319 L0 319 Z" fill="var(--footer)"/>
  </svg>
  <div class="brand abs" style="left:231px;top:2643px">Brava Nest</div>
  <span class="foot-social" style="left:877px"></span>
  <span class="foot-social" style="left:910px"></span>
  <span class="foot-social" style="left:943px"></span>
  <div class="foot-rule"></div>
  <p class="copyright">© All 2020 All rights reserved &nbsp;<b>Brava Nest</b></p>
</footer>

</body>
</html>
```